Web SITE design for new book

I need a unique design for a book my friend is releasing.

The home page needs to include:
A picture of the book
A spot for a video

Navigation:
Home
About the Book
Buy the Book
About the Author
Investing
Log In

The person awarded the project will also need to provide designs for the 5 other internal pages. They should be pretty straight forward.

Link to book design: https://www.filvantra.net/s/qmrt82kw7zpalvq/book-cover.png

Thanks!

```html
<!DOCTYPE html>
<html lang="en">
<head>
<meta charset="utf-8">
<title>The 5 Traps Every Saver Falls Into — Home</title>
<link rel="stylesheet" href="https://fonts.googleapis.com/css2?family=Raleway:wght@200;300;400&display=swap">
<style>
  :root {
    --gold: #a79442;
    --ghost: rgba(255, 255, 255, 0.075);
    --white: #ffffff;
    --book-light: #fbfbfb;
    --book-shade: #dcdcdc;
  }
  html, body {
    margin: 0;
    padding: 0;
    overflow: hidden;
  }
  .page {
    position: relative;
    width: 1200px;
    height: 800px;
    overflow: hidden;
    background: var(--gold);
    font-family: "Raleway", sans-serif;
    color: var(--white);
  }
  .backdrop-words span {
    position: absolute;
    font-weight: 200;
    color: var(--ghost);
    line-height: 1;
    white-space: nowrap;
    letter-spacing: 2px;
  }
  .w-five   { left: 150px; top: -10px;  font-size: 320px; }
  .w-traps  { left: 385px; top: 30px;   font-size: 130px; }
  .w-every  { left: 355px; top: 165px;  font-size: 72px; }
  .w-saver  { left: 580px; top: 262px;  font-size: 82px; }
  .w-falls  { left: 345px; top: 400px;  font-size: 150px; }
  .w-dodge  { left: 45px;  top: 548px;  font-size: 180px; }
  .w-saving { left: 85px;  top: 682px;  font-size: 50px; }
  .w-howto  { left: 628px; top: 590px;  font-size: 80px; }
  .w-steer  { left: 470px; top: 688px;  font-size: 88px; }
  .w-clear  { left: 990px; top: 676px;  font-size: 52px; }

  .main-nav {
    position: absolute;
    left: 0;
    top: 105px;
    width: 240px;
  }
  .main-nav ul {
    list-style: none;
    margin: 0;
    padding: 0;
  }
  .main-nav li {
    height: 70px;
    border-bottom: 2px solid var(--white);
    box-sizing: border-box;
  }
  .main-nav li:last-child { border-bottom: none; }
  .main-nav a {
    display: block;
    padding-right: 34px;
    text-align: right;
    font-size: 36px;
    font-weight: 300;
    line-height: 68px;
    color: var(--white);
    text-decoration: none;
  }

  .video-spot {
    position: absolute;
    left: 404px;
    top: 260px;
    width: 160px;
    text-align: center;
  }
  .play-button {
    display: block;
    margin: 0 auto;
  }
  .video-label {
    margin-top: 6px;
    font-size: 26px;
    font-weight: 300;
  }

  .book-visual {
    position: absolute;
    left: 715px;
    top: 80px;
  }
</style>
</head>
<body>
<main class="page">
  <div class="backdrop-words" aria-hidden="true">
    <span class="w-five">5</span>
    <span class="w-traps">TRAPS</span>
    <span class="w-every">EVERY</span>
    <span class="w-saver">SAVER</span>
    <span class="w-falls">FALLS</span>
    <span class="w-dodge">DODGE</span>
    <span class="w-saving">SAVING</span>
    <span class="w-howto">HOW TO</span>
    <span class="w-steer">STEERING</span>
    <span class="w-clear">CLEAR</span>
  </div>

  <nav class="main-nav">
    <ul>
      <li><a href="#">Home</a></li>
      <li><a href="#">Book</a></li>
      <li><a href="#">Buy</a></li>
      <li><a href="#">Author</a></li>
      <li><a href="#">Investing</a></li>
      <li><a href="#">Log In</a></li>
    </ul>
  </nav>

  <div class="video-spot">
    <svg class="play-button" width="96" height="96" viewBox="0 0 96 96" aria-hidden="true">
      <circle cx="48" cy="48" r="48" fill="var(--white)"/>
      <polygon points="36,26 36,70 72,48" fill="var(--gold)"/>
    </svg>
    <div class="video-label">Play video</div>
  </div>

  <svg class="book-visual" width="420" height="570" viewBox="0 0 420 570"
       role="img" aria-label="3D render of the hardcover book The 5 Traps Every Saver Falls Into and How to Dodge Them">
    <defs>
      <linearGradient id="coverFill" x1="0" y1="0" x2="1" y2="1">
        <stop offset="0" stop-color="var(--book-light)"/>
        <stop offset="1" stop-color="var(--book-shade)"/>
      </linearGradient>
    </defs>
    <polygon points="8,5 360,8 375,10 372,555 355,560 28,480" fill="url(#coverFill)"/>
  </svg>
</main>
</body>
</html>
```